BriskwayLane.com needs updated website design.

BriskwayLane.com offers individuals a quick, hassle-free way of selling their car, rv, or boat in the Sun City Center, FL area. We will come to the customer's place of choosing in order to give them an in-person offer for their car, rv, or boat. Looking for a website design that will allow users to input their vehicle details as well as their contact info in order to schedule a time and place for our staff to come make them an offer. Currently have an active site that can be referenced.

Target Market(s)

Older people who no longer need their cars.

Industry/Entity Type

Automotive

Coding

Coded - Design and coding required

Number of Pages Required

3 page

Font styles to use
Sans Serif

Colors
a1cd3a
33b8a4

Requirements
Must have
• Trustworthy theme, Emphasis on capturing contact info (contact form visible at all times). Standard privacy policy. Wordpress theme

```html
<!DOCTYPE html>
<html lang="en">
<head>
<meta charset="utf-8">
<title>BriskwayLane.com – Get Your Free In Person Cash Offer</title>
<link href="https://fonts.googleapis.com/css2?family=Montserrat:ital,wght@0,400;0,500;0,600;0,700;0,900;1,600;1,700;1,900&family=Roboto:wght@400;500&display=swap" rel="stylesheet">
<style>
:root{
  --navy:#06325e;
  --ink:#0b1b2e;
  --text:#3d4450;
  --line:#cfd3d8;
  --button:#63b3f5;
  --band:#eef6fd;
  --accent:#1ba4e6;
  --teal:#33b8a4;
  --green:#a1cd3a;
  --photo-light:#69c8f0;
  --photo-dark:#1c6792;
  --footer-text:#b8c7d8;
}
*{margin:0;padding:0;box-sizing:border-box}
html,body{width:853px;height:1200px;overflow:hidden;background:#fff}
body{position:relative;font-family:'Montserrat',sans-serif;color:var(--text)}
.abs{position:absolute}

.site-header{left:4px;top:0;width:849px;height:47px;background:#fff;box-shadow:0 1px 4px rgba(0,0,0,.06);z-index:3}
.brand{top:12px;display:flex;align-items:center;gap:5px}
.brand-dot{width:22px;height:22px;border-radius:50%;background:var(--accent)}
.brand-name{font-weight:700;font-size:11.5px;color:var(--navy);line-height:1}
.brand-tag{font-weight:700;font-size:6.5px;color:var(--navy);margin-top:2px;line-height:1}
.header-phone{top:20px;font-family:'Roboto',sans-serif;font-size:9px;color:#444;display:flex;align-items:center;gap:5px}
.main-nav{top:20px;font-weight:600;font-size:8.3px;color:var(--ink);letter-spacing:.1px}

.hero-photo{left:0;top:47px;width:853px;height:402px}
.hero-title{left:71px;top:80px;font-weight:900;font-style:italic;font-size:24.5px;line-height:25px;color:var(--ink);letter-spacing:-.2px}
.perk{font-size:8.3px;color:#555;white-space:nowrap}
.perk b{font-style:italic;font-weight:700;color:var(--ink)}

.offer-form{left:71px;top:194px;width:356px;height:225px;background:#fff;border:1px solid #dcdfe3;box-shadow:0 2px 8px rgba(0,0,0,.05)}
.form-heading{font-style:italic;font-weight:700;font-size:12px;color:#a3a6aa}
.field{border:1px solid var(--line);background:#fff;font-family:'Roboto',sans-serif;font-size:8.3px;color:#8a8e93;padding-left:6px;display:flex;align-items:center}
.submit{left:86px;top:374px;width:326px;height:34px;background:var(--button);color:#fff;font-family:'Roboto',sans-serif;font-weight:500;font-size:9.3px;letter-spacing:1px;display:flex;align-items:center;justify-content:center}

.reasons{left:0;top:449px;width:853px;height:248px;background:var(--band)}
.reason-icon{width:50px;height:50px}
.reason-title{width:300px;text-align:center;font-weight:600;font-size:10.7px;color:var(--ink)}
.reason-text{width:300px;text-align:center;font-size:9px;line-height:17.5px;color:#333}

.about-rule{left:403px;top:766px;width:47px;height:2px;background:var(--accent)}
.about-title{left:0;width:853px;top:781px;text-align:center;font-weight:900;font-style:italic;font-size:21px;color:var(--ink)}
.about-text{left:190px;width:473px;top:822px;text-align:center;font-size:11.8px;line-height:21.4px;color:#555;letter-spacing:.2px}

.site-footer{left:0;top:963px;width:853px;height:237px;background:var(--navy)}
.footer-heading{top:1018px;font-weight:900;font-style:italic;font-size:13px;color:#fff}
.contact-label{font-weight:600;font-size:9.5px;color:var(--footer-text)}
.contact-value{font-size:9.5px;color:var(--footer-text)}
.footer-link{left:345px;font-size:9.5px;color:var(--footer-text)}
.footer-brand{left:555px;top:1016px;display:flex;align-items:center;gap:6px}
.footer-brand .brand-dot{background:#fff;width:24px;height:24px}
.footer-brand .brand-name,.footer-brand .brand-tag{color:#fff}
.copyright{left:0;width:853px;top:1174px;text-align:center;font-size:8.3px;color:var(--footer-text)}
</style>
</head>
<body>

<header class="abs site-header">
  <div class="abs brand" style="left:67px">
    <span class="brand-dot"></span>
    <div>
      <div class="brand-name">BriskwayLane.com</div>
      <div class="brand-tag">Cash For Cars, Boats &amp; RVs</div>
    </div>
  </div>
  <div class="abs header-phone" style="left:233px">
    <svg width="9" height="9" viewBox="0 0 24 24"><path fill="#222" d="M6.6 10.8a15 15 0 0 0 6.6 6.6l2.2-2.2c.3-.3.7-.4 1-.2 1.1.4 2.3.6 3.6.6.6 0 1 .4 1 1V20c0 .6-.4 1-1 1A17 17 0 0 1 3 4c0-.6.4-1 1-1h3.5c.6 0 1 .4 1 1 0 1.3.2 2.5.6 3.6.1.3 0 .7-.2 1z"/></svg>
    555-014-2290
  </div>
  <nav>
    <span class="abs main-nav" style="left:533px">HOME</span>
    <span class="abs main-nav" style="left:593px">ABOUT US</span>
    <span class="abs main-nav" style="left:671px">CONTACT US</span>
    <span class="abs main-nav" style="left:760px">FAQ</span>
  </nav>
</header>

<svg class="abs hero-photo" viewBox="0 0 853 402" role="img" aria-label="Photo of a white SUV parked outdoors under trees, tinted blue">
  <defs>
    <linearGradient id="photoTone" x1="0" y1="0" x2="0.3" y2="1">
      <stop offset="0" stop-color="#69c8f0"/>
      <stop offset="0.55" stop-color="#3e9ccc"/>
      <stop offset="1" stop-color="#1c6792"/>
    </linearGradient>
  </defs>
  <polygon points="501,0 853,0 853,402 351,402" fill="url(#photoTone)"/>
</svg>

<h1 class="abs hero-title">GET YOUR FREE IN PERSON<br>CASH OFFER TODAY</h1>
<div class="abs perk" style="left:72px;top:143px"><b>Fast</b> – I'll be at your door today</div>
<div class="abs perk" style="left:238px;top:143px"><b>Friendly</b> – Trusted for over 25 years</div>
<div class="abs perk" style="left:72px;top:161px"><b>Fair</b> – Get a fair price for your vehicle</div>
<div class="abs perk" style="left:238px;top:161px"><b>Hassle Free</b> – I handle all the paperwork</div>

<form class="abs offer-form"></form>
<div class="abs form-heading" style="left:86px;top:203px">What are you trying to sell?</div>
<div class="abs field" style="left:86px;top:224px;width:326px;height:26px">Type of Vehicle
  <svg class="abs" style="right:8px;top:9px" width="11" height="7" viewBox="0 0 11 7"><path d="M1 1l4.5 4.5L10 1" fill="none" stroke="#333" stroke-width="1"/></svg>
</div>
<div class="abs field" style="left:86px;top:255px;width:118px;height:26px">Vehicle Make</div>
<div class="abs field" style="left:210px;top:255px;width:119px;height:26px">Vehicle Model</div>
<div class="abs field" style="left:335px;top:255px;width:77px;height:26px">Year</div>
<div class="abs form-heading" style="left:86px;top:290px">How can we reach you?</div>
<div class="abs field" style="left:86px;top:310px;width:201px;height:26px">Your Name</div>
<div class="abs field" style="left:293px;top:310px;width:119px;height:26px">Phone</div>
<div class="abs field" style="left:86px;top:342px;width:237px;height:26px">Email</div>
<div class="abs field" style="left:329px;top:342px;width:83px;height:26px">ZIP Code</div>
<div class="abs submit">SCHEDULE AN APPOINTMENT</div>

<section class="abs reasons"></section>
<svg width="0" height="0" style="position:absolute">
  <defs>
    <linearGradient id="ring" x1="0" y1="1" x2="1" y2="0">
      <stop offset="0" stop-color="#33b8a4"/>
      <stop offset="1" stop-color="#a1cd3a"/>
    </linearGradient>
  </defs>
</svg>
<svg class="abs reason-icon" style="left:125px;top:507px" viewBox="0 0 50 50">
  <circle cx="25" cy="25" r="23.5" fill="none" stroke="url(#ring)" stroke-width="1.2"/>
  <path d="M30 18c-1-2-3-3-5-3-3 0-5 1.6-5 4s2 3.3 5 4 5 2 5 4.5-2 4-5 4c-2.5 0-4.5-1-5.3-3M25 12v26" fill="none" stroke="url(#ring)" stroke-width="1.2"/>
</svg>
<svg class="abs reason-icon" style="left:402px;top:507px" viewBox="0 0 50 50">
  <circle cx="25" cy="25" r="23.5" fill="none" stroke="url(#ring)" stroke-width="1.2"/>
  <path d="M13 30v-5l3-7h18l3 7v5zM16 25h18M14 30v3h4v-3M32 30v3h4v-3" fill="none" stroke="url(#ring)" stroke-width="1.2"/>
  <circle cx="18" cy="27.5" r="1.2" fill="none" stroke="url(#ring)"/><circle cx="32" cy="27.5" r="1.2" fill="none" stroke="url(#ring)"/>
</svg>
<svg class="abs reason-icon" style="left:660px;top:507px" viewBox="0 0 50 50">
  <circle cx="25" cy="25" r="23.5" fill="none" stroke="url(#ring)" stroke-width="1.2"/>
  <path d="M15 15l2-2 3 3-1 1 14 14 2 0 3 3-3 3-3-3v-2L18 18l-1 1zM35 15a4 4 0 0 0-5 5L15 33l2 2 13-15a4 4 0 0 0 5-5l-2 2-2-2z" fill="none" stroke="url(#ring)" stroke-width="1.1" stroke-linejoin="round"/>
</svg>
<h3 class="abs reason-title" style="left:0;top:576px">GOT AN OLD CLUNKER?</h3>
<p class="abs reason-text" style="left:0;top:592px">I'll Buy It! – Turn it into cash today!</p>
<h3 class="abs reason-title" style="left:277px;top:576px">GOT A NICE CAR YOU JUST DON'T NEED?</h3>
<p class="abs reason-text" style="left:277px;top:592px">I'll Buy It! – Stop wasting money on insurance,<br>registration and maintenance costs!</p>
<h3 class="abs reason-title" style="left:535px;top:576px">GOT A CAR THAT NEEDS REPAIRS?</h3>
<p class="abs reason-text" style="left:535px;top:592px">I'll Buy It! – No matter what the issue is<br>I'll come take it away today!</p>

<div class="abs about-rule"></div>
<h2 class="abs about-title">ABOUT US</h2>
<p class="abs about-text">We offer the most convenient way of selling your vehicle. We will come to<br>you at a place of your choosing, i.e. home, office, or any other public place.<br>We will give you an in person cash offer on the spot.</p>

<footer class="abs site-footer"></footer>
<h4 class="abs footer-heading" style="left:71px">CONTACT US</h4>
<svg class="abs" style="left:71px;top:1056px" width="9" height="9" viewBox="0 0 24 24"><path fill="#b8c7d8" d="M6.6 10.8a15 15 0 0 0 6.6 6.6l2.2-2.2c.3-.3.7-.4 1-.2 1.1.4 2.3.6 3.6.6.6 0 1 .4 1 1V20c0 .6-.4 1-1 1A17 17 0 0 1 3 4c0-.6.4-1 1-1h3.5c.6 0 1 .4 1 1 0 1.3.2 2.5.6 3.6.1.3 0 .7-.2 1z"/></svg>
<div class="abs contact-label" style="left:93px;top:1052px">Phone Number</div>
<div class="abs contact-value" style="left:93px;top:1070px">555-014-2290</div>
<svg class="abs" style="left:71px;top:1109px" width="10" height="8" viewBox="0 0 10 8"><rect width="10" height="8" fill="#b8c7d8"/><path d="M0 0l5 4 5-4" fill="none" stroke="#06325e" stroke-width="1"/></svg>
<div class="abs contact-label" style="left:93px;top:1105px">Email Address</div>
<div class="abs contact-value" style="left:93px;top:1123px">info@briskwaylane.com</div>

<h4 class="abs footer-heading" style="left:345px">NAVIGATE</h4>
<div class="abs footer-link" style="top:1052px">Home</div>
<div class="abs footer-link" style="top:1073px">About Us</div>
<div class="abs footer-link" style="top:1094px">Contact Us</div>
<div class="abs footer-link" style="top:1116px">FAQ</div>

<div class="abs footer-brand">
  <span class="brand-dot"></span>
  <div>
    <div class="brand-name" style="font-size:12px">BriskwayLane.com</div>
    <div class="brand-tag" style="font-size:7px">Cash For Cars, Boats &amp; RVs</div>
  </div>
</div>
<div class="abs contact-value" style="left:558px;top:1059px">Fast – Fair – Friendly</div>
<div class="abs contact-value" style="left:558px;top:1081px">Trusted Over 25 Years</div>

<div class="abs copyright">Copyright © 2020. All rights reserved.</div>

</body>
</html>
```